Label design for an exciting new Vodka brand

We need a label design for a dynamic new Vodka brand called 'Pale lantern Vodka'. It is a crisp and versatile liquid with a clean and smooth finish. It should appeal to 21-39 year olds, with a slight female skew. Colours, fonts and styles should be modern and relatively neutral - take inspiration from the brand pictures attached.

Target Market(s)

21-39 year olds, both male and female, but with a slight female skew

```html
<!DOCTYPE html>
<html lang="en">
<head>
<meta charset="utf-8">
<title>Pale Lantern Vodka — Label</title>
<link rel="stylesheet" href="https://fonts.googleapis.com/css2?family=Cormorant+Garamond:wght@500&family=Montserrat:wght@500;600;700&family=Russo+One&display=swap">
<style>
  :root {
    --bg: #eef1f7;
    --label: #f7f9fc;
    --ink: #2b4ea6;
    --ink-soft: #4a68b4;
    --band-dark: #0d2a78;
    --band-mid: #2f62c0;
    --band-light: #6e9be0;
    --rule: #9fb0d6;
    --white: #ffffff;
  }
  * { box-sizing: border-box; margin: 0; padding: 0; }
  html, body {
    width: 960px; height: 1200px; overflow: hidden;
    background: var(--bg);
  }
  .label {
    position: absolute; left: 112px; top: 0;
    width: 736px; height: 1200px;
    background: var(--label);
    font-family: "Montserrat", sans-serif;
    color: var(--ink);
  }
  .ornament {
    position: absolute; left: 143px; top: 50px;
    width: 450px; height: 150px;
    border-radius: 75px 75px 20px 20px;
    background: radial-gradient(ellipse at 50% 70%, #c9d6ef 0%, #e4eaf6 60%, var(--label) 100%);
  }
  .brand-mark {
    position: absolute; left: 298px; top: 262px;
    width: 140px; height: 140px; border-radius: 50%;
    background: var(--ink);
  }
  .brand-name {
    position: absolute; left: 0; top: 420px; width: 100%;
    text-align: center;
    font-family: "Cormorant Garamond", serif;
    font-weight: 500; font-size: 104px; line-height: 150px;
    color: var(--ink-soft);
  }
  .band {
    position: absolute; left: 0; top: 590px;
    width: 100%; height: 280px;
    background: linear-gradient(90deg, var(--band-dark) 0%, var(--band-mid) 35%, var(--band-light) 50%, var(--band-mid) 65%, var(--band-dark) 100%);
    border-top: 10px solid #c3cde3;
    border-bottom: 10px solid #c3cde3;
  }
  .band-title {
    position: absolute; left: 0; top: 0; width: 100%; height: 100%;
    display: flex; align-items: center; justify-content: center;
    font-family: "Russo One", sans-serif;
    font-size: 190px; letter-spacing: 4px;
    color: var(--white);
  }
  .variant {
    position: absolute; left: 40px; top: 910px; width: 656px;
    display: flex; align-items: center; justify-content: center; gap: 28px;
  }
  .variant-lines { width: 120px; height: 24px; }
  .variant-name { font-weight: 700; font-size: 48px; letter-spacing: 1px; color: var(--ink-soft); }
  .rule {
    position: absolute; left: 105px; width: 526px; height: 2px;
    background: var(--rule);
  }
  .rule--top { top: 982px; }
  .rule--bottom { top: 1040px; }
  .tagline {
    position: absolute; left: 0; top: 988px; width: 100%;
    text-align: center;
    font-weight: 500; font-size: 34px; line-height: 50px; letter-spacing: 1px;
    color: var(--ink-soft);
  }
  .facts {
    position: absolute; left: 105px; top: 1060px; width: 526px;
    display: grid; grid-template-columns: 1fr 2px 3.2fr 2px 1fr;
    align-items: center; text-align: center;
  }
  .facts-divider { height: 60px; background: var(--rule); }
  .facts-small { font-weight: 500; font-size: 18px; line-height: 26px; color: var(--ink-soft); }
  .facts-main { font-weight: 600; font-size: 30px; line-height: 38px; color: var(--ink); }
</style>
</head>
<body>
  <main class="label">
    <div class="ornament" role="img" aria-label="Blue filigree crown flourish ornament"></div>
    <div class="brand-mark" aria-hidden="true"></div>
    <h1 class="brand-name">Pale Lantern</h1>

    <section class="band">
      <div class="band-title">VODKA</div>
    </section>

    <div class="variant">
      <svg class="variant-lines" viewBox="0 0 120 24" aria-hidden="true">
        <g stroke="#9fb0d6" stroke-width="2"><line x1="0" y1="4" x2="120" y2="4"/><line x1="10" y1="12" x2="120" y2="12"/><line x1="0" y1="20" x2="120" y2="20"/></g>
      </svg>
      <span class="variant-name">ORIGINAL</span>
      <svg class="variant-lines" viewBox="0 0 120 24" aria-hidden="true">
        <g stroke="#9fb0d6" stroke-width="2"><line x1="0" y1="4" x2="120" y2="4"/><line x1="0" y1="12" x2="110" y2="12"/><line x1="0" y1="20" x2="120" y2="20"/></g>
      </svg>
    </div>
    <div class="rule rule--top"></div>
    <p class="tagline">CRISP AND VERSATILE LIQUID</p>
    <div class="rule rule--bottom"></div>

    <div class="facts">
      <div class="facts-small">40%<br>vol</div>
      <div class="facts-divider"></div>
      <div class="facts-main">ALL-NATURAL<br>COLL BEFORE</div>
      <div class="facts-divider"></div>
      <div class="facts-small">750<br>ml</div>
    </div>
  </main>
</body>
</html>
```